American Ingenuity + Italian Design = RTB
International consulting services from fine arts/advertising/construction & special events. A new company that will find the right connections to get your job done.

Card should include -
1. Company Name with logo: rosalind tavore Enterprises LLC
2. Address: 218 Dunmore Lane, Highland Springs, VA 23081
3. Phone Number: 804.512.3096 (US)
4. Tagline: American Ingenuity + Italian Style + RTB (you can improve on this idea)
5. web address to be added eventually

Likes: airplanes and boats to give the idea of movement & international ability
Logo: if you have an idea to adjust the colors, we are open to that. Rosalind likes blues, but other colors didn't seem to work; remember this will print 4c in most cases)
Updates

I have uploaded the logo on it's own. Typical business card size for the US is 3.5" x 2", but doesn't have to be that size. the flyer was just for reference of something else that was done and to give some background. I hope that didn't confuse anyone.

Thank you all for the amazing work in the tight deadline. We will be reviewing everything today and will provide feedback by tomorrow. I will also pass this site on to anyone I know looking for design work.

website address rosalindtavore.example email rosalind@rosalindtavore.example Italian number +39 347 861 2054 USA 1 804 512 3096 International Consulting Services American Ingenuity. Italian Design. rtB These are the vital elements for the card. In addition please note the new fotos should have been uploaded. Best Regards

Target Market(s)

Companies or individuals that want to bring the Italian flair to the US or American know how to Italian projects. This can range from a bride planning a destination wedding, an interior designer looking to add pieces or knowledge to their project, or an investor looking to buy property to invest and build.

Industry/Entity Type

Construction

Requirements
Must have
• 1. Company Name with logo: rosalind tavore Enterprises LLC
+39 347 861 2054 (Italia)
Nice to have
• incorporate the idea of international ability; airplanes (like the wing in the background of the logo)
Should not have
• not overly decorative

```html
<!DOCTYPE html>
<html lang="en">
<head>
<meta charset="utf-8">
<title>rosalind tavore Enterprises LLC — Business Card</title>
<link href="https://fonts.googleapis.com/css2?family=Tinos:wght@400;700&display=swap" rel="stylesheet">
<style>
  :root {
    --backdrop: #e9e9eb;
    --card-front: #ffffff;
    --card-back: #f1f0f2;
    --brand: #7a1f16;
    --ink: #2b2b2b;
    --frame: #5a2a20;
  }
  * { box-sizing: border-box; margin: 0; padding: 0; }
  html, body {
    width: 1200px; height: 960px; overflow: hidden;
    background: var(--backdrop);
    font-family: "Tinos", "Times New Roman", serif;
  }
  .sheet {
    width: 1200px; height: 960px;
    display: flex; flex-direction: column;
    align-items: center; justify-content: center; gap: 60px;
  }
  .card {
    width: 700px; height: 400px;
    border-radius: 10px;
    box-shadow: 0 2px 6px rgba(0,0,0,0.12);
    position: relative;
  }
  .card--front {
    background: var(--card-front);
    display: flex; align-items: center; justify-content: center;
  }
  .brand-name {
    display: flex; align-items: center; gap: 14px;
    color: var(--brand);
    font-weight: 400;
  }
  .brand-name__mark {
    width: 18px; height: 18px; border-radius: 50%;
    background: var(--brand);
  }
  .card--front .brand-name { font-size: 38px; }
  .card--back {
    background: var(--card-back);
    padding: 30px 60px;
  }
  .logo-frame {
    width: 250px; height: 110px;
    margin: 0 auto;
    border: 1.5px solid var(--frame);
    background: var(--card-front);
    display: flex; align-items: center; justify-content: center;
  }
  .logo-frame .brand-name { font-size: 15px; gap: 8px; }
  .logo-frame .brand-name__mark { width: 9px; height: 9px; }
  .tagline {
    margin-top: 22px;
    text-align: center;
    color: var(--brand);
    font-weight: 700;
    font-size: 21px;
    letter-spacing: 0.3px;
  }
  .contact {
    margin-top: 26px;
    list-style: none;
    font-size: 17px;
    color: var(--ink);
    line-height: 1.45;
  }
  .contact__row { display: flex; }
  .contact__label { width: 60px; font-weight: 700; }
</style>
</head>
<body>
  <main class="sheet">
    <section class="card card--front" aria-label="Card front">
      <div class="brand-name">
        <span class="brand-name__mark" aria-hidden="true"></span>
        <span>rosalind tavore Enterprises LLC</span>
      </div>
    </section>

    <section class="card card--back" aria-label="Card back">
      <div class="logo-frame">
        <div class="brand-name">
          <span class="brand-name__mark" aria-hidden="true"></span>
          <span>rosalind tavore Enterprises LLC</span>
        </div>
      </div>
      <p class="tagline">American Ingenuity + Italian Style + RTB</p>
      <ul class="contact">
        <li class="contact__row"><span class="contact__label">A:</span><span>218 Dunmore Lane, Highland Springs, VA 23081</span></li>
        <li class="contact__row"><span class="contact__label">P:</span><span>804.512.3096 (US)</span></li>
        <li class="contact__row"><span class="contact__label"></span><span>+39 347 861 2054 (Italia)</span></li>
        <li class="contact__row"><span class="contact__label">E:</span><span>rosalind@rosalindtavore.example</span></li>
        <li class="contact__row"><span class="contact__label">W:</span><span>www.rosalindtavore.example</span></li>
      </ul>
    </section>
  </main>
</body>
</html>
```